Business Card (double-sided) and Stationary Design for dental office

1) Business Card Design: We need a business card design for a dental specialty office.
Texts should contain:
The name of our office "Maplecrest Family Orthodontics"
Tagline: "Specialist in Orthodontic and Maxillofacial Orthopedics"
Tag line: "Creating "Dorvaling" smiles for Children and Adults"
Doctor name: "Doctor Name"
Office Address:
"123 Street Name
City, State Zip code"
Office email address: office@maplecrestfamily.com
Website: www.maplecrestfamily.com

We will provide the full office address once the design is selected
Theme: beach, paradise, coastal, wave
We would like to have some creativity in design. Some acceptable ideas: front page: logo and office name. Back page: more detail information, and map to office in form of an island. Please see sample from our other location, but you DON'T HAVE TO USE OR COPY THE SAME CONCEPT.

IF POSSIBLE, PLEASE SUBMIT AT LEAST TWO CONCEPTS: ONE WITH THE BACK LOOKING SIMILAR TO WHAT IS IN THE SAMPLE, AND ONE DIFFERENT.

Color: designer to choose. We have different shade of blues and sand color in our office. Please see logo.

2) Please also design a matching set of stationary that compliment the business card and our logo.

Target Market(s)

Dental

Contact Information for Business Card

See descriptions

Font styles to use
Other font styles liked:
• Matching texts in logo

Colors
0054AA
0677BA
7BADD7
CADEEF
E8F1F8
0094D4
00A9DD
6FCCEA
C7EBF8
E9F6FB
00AB8E
00BBA5
67D7C9
C6EFE9
E9F9F6

Requirements
Must have
• Double-sided
Nice to have
• Beach coastal theme
Should not have
• Any shape or drawing of of tooth or teeth. We don’t need these. You don't necessarily have to just cut and paste the logo art and text as a whole, you have the liberty to rearrange the text.

```html
<!DOCTYPE html>
<html lang="en">
<head>
<meta charset="utf-8">
<title>Maplecrest Family Orthodontics – Business Card</title>
<link rel="stylesheet" href="https://fonts.googleapis.com/css2?family=Raleway:wght@400;500;700;800&display=swap">
<style>
  :root {
    --backdrop: #2b2b2b;
    --teal: #3a90a8;
    --teal-deep: #2f7f97;
    --mint: #67d7c9;
    --white: #ffffff;
    --ink-teal: #3a8fa8;
    --sky-top: #3f86c9;
    --sky-low: #9cc9e8;
    --sea: #3fc3c0;
    --sea-light: #8fdcd3;
    --sand: #cfc3a4;
    --sand-deep: #b5a884;
    --panel: rgba(255, 255, 255, 0.78);
    --pin: #1f5f8f;
  }
  * { box-sizing: border-box; margin: 0; padding: 0; }
  html, body {
    width: 1200px; height: 1015px; overflow: hidden;
    background: var(--backdrop);
    font-family: "Raleway", sans-serif;
  }
  .sheet {
    width: 1200px; height: 1015px;
    display: flex; flex-direction: column; align-items: center; justify-content: center;
    gap: 44px;
  }
  .card {
    position: relative;
    width: 760px; height: 434px;
    overflow: hidden;
    box-shadow: 0 12px 30px rgba(0,0,0,0.5);
  }

  /* Back side: beach scene with appointment panel */
  .card--back .beach-scene {
    position: absolute; inset: 0;
    background: linear-gradient(180deg,
      var(--sky-top) 0%, var(--sky-low) 30%,
      var(--sea) 38%, var(--sea-light) 52%,
      var(--sand) 62%, var(--sand-deep) 100%);
  }
  .appointment-panel {
    position: absolute; left: 170px; top: 40px;
    width: 440px; height: 230px;
    background: var(--panel);
    display: flex; flex-direction: column; align-items: center;
    padding-top: 58px;
  }
  .appointment-title {
    color: var(--ink-teal); font-weight: 500; font-size: 30px; letter-spacing: 0.5px;
  }
  .appointment-line {
    width: 320px; height: 1px; background: #9aa6ad; margin-top: 60px;
  }
  .location-label {
    position: absolute; left: 50%; top: 292px; transform: translateX(-50%);
    display: flex; align-items: center; gap: 6px;
    color: #1e2a33; font-weight: 500; font-size: 22px;
  }
  .location-label svg { width: 18px; height: 24px; }

  /* Front side: contact details and brand circle */
  .card--front { background: var(--teal); }
  .brand-circle { position: absolute; inset: 0; }
  .brand {
    position: absolute; left: 455px; top: 90px; width: 290px;
    display: flex; flex-direction: column; align-items: center; gap: 14px;
    text-align: center;
  }
  .brand-dot { width: 64px; height: 64px; border-radius: 50%; background: var(--teal); }
  .brand-name {
    color: var(--teal); font-weight: 700; font-size: 30px; line-height: 1.15;
  }
  .contact {
    position: absolute; left: 46px; top: 52px; color: var(--white);
  }
  .contact-name { font-weight: 800; font-size: 32px; line-height: 1.05; }
  .contact-role { font-weight: 500; font-size: 20px; margin-bottom: 22px; }
  .contact-address { font-size: 19px; line-height: 1.25; margin-bottom: 18px; }
  .contact-row { display: flex; align-items: center; gap: 10px; font-size: 19px; line-height: 1.35; }
  .contact-row svg { width: 18px; height: 18px; flex: none; }
  .tagline {
    position: absolute; left: 46px; bottom: 36px; color: var(--white);
    text-transform: uppercase; line-height: 1.2;
  }
  .tagline-smiles { font-weight: 500; font-size: 19px; margin-bottom: 16px; }
  .tagline-specialist { font-weight: 800; font-size: 19px; }
</style>
</head>
<body>
<main class="sheet">

  <section class="card card--back" aria-label="Business card back">
    <div class="beach-scene" role="img" aria-label="Painted tropical beach with palm trees, turquoise sea, a wooden boat on the sand and a hand-drawn route map to the office"></div>
    <div class="appointment-panel">
      <p class="appointment-title">Next Appointment</p>
      <div class="appointment-line"></div>
    </div>
    <p class="location-label">
      <svg viewBox="0 0 18 24" aria-hidden="true"><path d="M9 0C4 0 0 4 0 9c0 6.5 9 15 9 15s9-8.5 9-15c0-5-4-9-9-9z" fill="var(--pin)"/><circle cx="9" cy="9" r="3.5" fill="#fff"/></svg>
      Maplecrest Family
    </p>
  </section>

  <section class="card card--front" aria-label="Business card front">
    <svg class="brand-circle" viewBox="0 0 760 434" aria-hidden="true">
      <circle cx="612" cy="190" r="262" fill="none" stroke="var(--mint)" stroke-width="6"/>
      <circle cx="622" cy="186" r="258" fill="var(--white)"/>
    </svg>
    <div class="brand">
      <span class="brand-dot"></span>
      <p class="brand-name">Maplecrest Family Orthodontics</p>
    </div>

    <div class="contact">
      <p class="contact-name">Daniel Reyes</p>
      <p class="contact-role">Managing Director</p>
      <p class="contact-address">123 Street Name<br>City, State Zip code</p>
      <p class="contact-row">
        <svg viewBox="0 0 18 18" aria-hidden="true"><rect x="1" y="4" width="16" height="11" fill="none" stroke="#fff" stroke-width="1.5"/><path d="M1 4l8 6 8-6" fill="none" stroke="#fff" stroke-width="1.5"/></svg>
        office@maplecrestfamily.com
      </p>
      <p class="contact-row">
        <svg viewBox="0 0 18 18" aria-hidden="true"><circle cx="9" cy="9" r="7.5" fill="none" stroke="#fff" stroke-width="1.5"/><ellipse cx="9" cy="9" rx="3.2" ry="7.5" fill="none" stroke="#fff" stroke-width="1.2"/><path d="M1.5 9h15M3 5h12M3 13h12" stroke="#fff" stroke-width="1.2"/></svg>
        www.maplecrestfamily.com
      </p>
    </div>

    <div class="tagline">
      <p class="tagline-smiles">Creating Dorvaling smiles<br>for children and adults</p>
      <p class="tagline-specialist">Specialist in orthodontic<br>and maxillofacial orthopedics</p>
    </div>
  </section>

</main>
</body>
</html>
```